Architecture office 10 pages brochure for investors

We need a multi-page brochure (10pg) for our small architectural office.
After the long real estate crisis in Greece we're intend to reborn our architectural planning services, to relocate our targets and to communicate the philosophy in the new era of commercial buildings:
Modern architectural language, Highly energy efficient buildings with green and passive oriented design and functional details. Multifamily housing, Office buildings, Hotels, Refurbishment and Interiors from a group of new architects collaborators and an experienced leader.
We need fresh, clever styling with minimal expression and reach meanings. Written in two languages (ENG-GR) the fonts must be compatible. The solution of an digital and non-printed brochure, for on-line sharing, its a possibility and maybe unlock animated and / or AR solutions. The green color -as attached- will be appreciated.

Please provide your professional opinion about the set up of the pages.
An idea given: minimal frontpage, 2-3nd pages "about us" and "contents with photo and some minor text, and every next page refers one selected project with photo and some text for two languages (4-7 pages projects), pages 8-9 listed works-projects, collaborators, clients.
Updates

low design entries -one entry as 4 projects- , low quality, not satisfying the wills

Target Market(s)

investors in commercial buildings, private clients, energy efficiency

Industry/Entity Type

Architecture

Font styles to use
Sans Serif
Other font styles liked:
• greek compatible

Requirements
Must have
• clear - minimal design, photos, illustrations, text, contents.
• some of the projects can find them in attached link,
Nice to have
• dynamic lines, hand drawing sketches
• maybe the building design process: thoughts, sketch, hand design, cad, collaboration with other engineers, 3d renderings, animations ....
Should not have
• art deco, romantic styles, full red or basic contrasting colors (red/green, purple/orange etc)

```html
<!DOCTYPE html>
<html lang="en">
<head>
<meta charset="utf-8">
<title>Verda Studio – Brochure Spreads</title>
<link href="https://fonts.googleapis.com/css2?family=Montserrat:wght@400;500;600&display=swap" rel="stylesheet">
<style>
:root{
  --stage:#565656;
  --page-left:#f7f7f7;
  --page-right:#f1f1f1;
  --green:#b6bf45;
  --ink:#2b2b2b;
  --body:#555;
  --muted:#9c9c9c;
  --icon:#8a8a8a;
  --white:#fff;
}
*{box-sizing:border-box;margin:0;padding:0}
html,body{width:907px;height:1200px;overflow:hidden}
body{background:var(--stage);font-family:'Montserrat',sans-serif;color:var(--ink);position:relative}
.spread{position:absolute;left:83px;width:741px;height:480px;
  background:linear-gradient(to right,var(--page-left) 0 371px,var(--page-right) 371px 100%);
  box-shadow:0 6px 14px rgba(0,0,0,.35)}
.spread--cover{top:90px}
.spread--about{top:638px}
.abs{position:absolute}

/* cover spread */
.side-band{left:0;top:20px;width:19px;height:440px;background:var(--green)}
.brand{display:flex;align-items:center;gap:5px;color:var(--green);font-weight:600;letter-spacing:.2px;white-space:nowrap}
.brand__dot{width:9px;height:9px;border-radius:50%;background:var(--green);flex:none}
.brand--top{left:412px;top:48px;font-size:15px}
.brand--top .brand__dot{width:12px;height:12px}
.brand--small{left:46px;top:313px;font-size:10px}
.cover-photo{left:175px;top:111px;width:468px;height:297px;
  background:
    radial-gradient(ellipse 38% 30% at 28% 62%,rgba(120,160,200,.55),transparent 70%),
    radial-gradient(ellipse 45% 40% at 72% 48%,rgba(190,225,245,.55),transparent 70%),
    radial-gradient(ellipse 60% 22% at 60% 88%,rgba(150,205,240,.6),transparent 70%),
    linear-gradient(135deg,#3a9fdc 0%,#52b2e8 40%,#6cc0ee 62%,#3a8fcf 100%)}
.hero-panel{left:558px;top:20px;width:165px;height:440px;background:var(--green)}
.hero-panel__tint{left:558px;top:111px;width:85px;height:297px;background:rgba(70,110,130,.14)}
.hero-title{left:580px;top:164px;color:var(--white);font-weight:500;font-size:22.5px;line-height:27px;letter-spacing:.4px}
.hero-rule{left:581px;top:280px;width:12px;height:2px;background:var(--white)}
.hero-lede{left:580px;top:295px;color:var(--white);font-size:8.8px;line-height:11.8px;white-space:nowrap}
.contact-title{left:46px;top:352px;font-size:11px;font-weight:400;letter-spacing:.2px}
.contact-title span,.section-title span{color:var(--green)}
.short-rule{width:8px;height:1.5px;background:var(--green)}
.contact-list{left:38px;top:380px;list-style:none;font-size:6.3px;line-height:8.4px;color:var(--body)}
.contact-list li{display:flex;gap:3px;margin-bottom:6px}
.contact-list svg{width:6px;height:6px;flex:none;margin-top:1px}
.social{left:236px;top:434px;display:flex;gap:8.5px}
.social span{width:12.5px;height:12.5px;border-radius:50%;background:var(--icon)}
.spine-rule{left:418px;top:385px;width:1px;height:95px;background:var(--green)}
.spine-url{left:424px;top:470px;transform:rotate(-90deg);transform-origin:left top;font-size:6px;font-weight:500;white-space:nowrap}

/* about spread */
.about-photo{left:40px;top:40px;width:452px;height:222px;
  background:
    radial-gradient(ellipse 30% 28% at 70% 48%,rgba(240,238,230,.85),transparent 70%),
    radial-gradient(ellipse 34% 22% at 30% 55%,rgba(230,226,215,.75),transparent 70%),
    radial-gradient(ellipse 22% 26% at 58% 58%,rgba(196,170,125,.7),transparent 70%),
    radial-gradient(ellipse 30% 14% at 80% 80%,rgba(215,170,60,.45),transparent 70%),
    linear-gradient(to bottom,#4d7bc6 0%,#7fa5dc 18%,#b8cde6 30%,#d9d4c4 42%,#c9b592 62%,#8f9a78 76%,#6f8a5a 82%,#8b8e92 90%,#7a7d82 100%)}
.section-title{left:40px;top:288px;font-size:14.5px;font-weight:400;letter-spacing:.2px}
.section-title span{font-weight:600}
.copy{font-size:5.9px;line-height:8.3px;color:var(--body);text-align:justify}
.copy p+p{margin-top:12px}
.about-copy{left:40px;top:325px;width:284px}
.page-foot{display:flex;align-items:center;gap:4px;font-size:4.8px;font-weight:500;width:284px}
.page-foot__line{flex:1;height:.7px;background:var(--green)}
.page-foot__num{width:8px;height:8px;border-radius:50%;background:var(--green);color:var(--white);font-size:4px;display:flex;align-items:center;justify-content:center}
.foot-left{left:40px;top:453px}
.foot-right{left:413px;top:453px}
.top-rule{left:519px;top:0;width:1px;height:109px;background:var(--green)}
.feature-title{left:538px;top:42px;color:var(--green);font-weight:500;font-size:14.3px;line-height:17px;letter-spacing:.2px}
.feature-copy{left:538px;top:124px;width:159px}
.points-title{left:538px;top:295px;font-size:8.4px;line-height:10.4px;font-weight:500}
.points{left:539px;top:332px;list-style:none}
.points li{display:flex;gap:10px;height:35.5px}
.points__num{width:13px;height:13px;background:var(--green);color:var(--white);font-size:7px;display:flex;align-items:center;justify-content:center;flex:none}
.points p{font-size:5.5px;line-height:8.3px;color:var(--body);white-space:nowrap;margin-top:-1px}
.quote-mark{color:#c4c4c4;font-size:34px;line-height:1;font-weight:600}
.quote-open{left:412px;top:290px}
.quote-close{left:476px;top:402px}
.pull-quote{left:413px;top:314px;color:var(--muted);font-size:10.2px;line-height:13.3px;letter-spacing:.2px;white-space:nowrap}
</style>
</head>
<body>

<section class="spread spread--cover">
  <div class="abs side-band"></div>
  <div class="abs brand brand--top"><span class="brand__dot"></span>verda studio</div>
  <div class="abs cover-photo" role="img" aria-label="Hand sketching an architectural line drawing over a rendered modern house, in blue tones"></div>
  <div class="abs hero-panel"></div>
  <div class="abs hero-panel__tint"></div>
  <h1 class="abs hero-title">LOREM<br>IPSUM<br>DOLOR SIT<br>AMET</h1>
  <div class="abs hero-rule"></div>
  <p class="abs hero-lede">consectetur adipiscing<br>elit, sed do eiusmod tempor<br>incididunt ut labore et<br>dolore magna aliqua</p>

  <div class="abs brand brand--small"><span class="brand__dot"></span>verda studio</div>
  <h2 class="abs contact-title">CONTACT <span>INFO</span></h2>
  <div class="abs short-rule" style="left:47px;top:370px"></div>
  <ul class="abs contact-list">
    <li><svg viewBox="0 0 10 10"><path d="M5 1a3 3 0 0 1 3 3c0 2-3 5-3 5S2 6 2 4a3 3 0 0 1 3-3z" fill="none" stroke="#b6bf45" stroke-width="1.2"/></svg><span>Address Line 1, Address Line 1<br>Address Line 2</span></li>
    <li><svg viewBox="0 0 10 10"><rect x="1" y="2.5" width="8" height="5.5" fill="none" stroke="#b6bf45" stroke-width="1"/><path d="M1 2.5l4 3 4-3" fill="none" stroke="#b6bf45" stroke-width="1"/></svg><span>hello@verdastudio.example</span></li>
    <li><svg viewBox="0 0 10 10"><circle cx="5" cy="5" r="4" fill="none" stroke="#b6bf45" stroke-width="1"/><path d="M3.5 3.2l1 1-.5.6 1.3 1.3.6-.5 1 1-.8.8C4.8 7.2 2.8 5.2 2.7 4z" fill="#b6bf45"/></svg><span>0123 456 789</span></li>
    <li><svg viewBox="0 0 10 10"><circle cx="5" cy="5" r="4" fill="none" stroke="#b6bf45" stroke-width="1"/><path d="M1 5h8M5 1c-2 2.5-2 5.5 0 8M5 1c2 2.5 2 5.5 0 8" fill="none" stroke="#b6bf45" stroke-width=".8"/></svg><span>www.verdastudio.example</span></li>
  </ul>
  <div class="abs social" aria-label="Social links"><span></span><span></span><span></span><span></span></div>
  <div class="abs spine-rule"></div>
  <div class="abs spine-url">www.verdastudio.example</div>
</section>

<section class="spread spread--about">
  <div class="abs about-photo" role="img" aria-label="Rendering of a modern two-storey residential building with balconies under a blue sky"></div>
  <h2 class="abs section-title">ABOUT <span>US</span></h2>
  <div class="abs short-rule" style="left:41px;top:311px"></div>
  <div class="abs copy about-copy">
    <p>Lorem ipsum dolor sit amet, consectetur adipiscing elit, sed do eiusmod tempor incididunt ut labore et dolore magna aliqua. Ut enim ad minim veniam, quis nostrud exercitation ullamco laboris nisi ut aliquip ex ea commodo consequat. Duis aute irure dolor in reprehenderit in voluptate velit esse cillum dolore eu fugiat nulla pariatur. Excepteur sint occaecat cupidatat non proident, sunt in culpa qui officia deserunt mollit anim id est laborum.</p>
    <p>Sed ut perspiciatis unde omnis iste natus error sit voluptatem accusantium doloremque laudantium, totam rem aperiam, eaque ipsa quae ab illo inventore veritatis et quasi architecto beatae vitae dicta sunt explicabo. Nemo enim ipsam voluptatem quia voluptas sit aspernatur aut odit aut fugit, sed quia consequuntur magni dolores eos qui ratione voluptatem sequi nesciunt.</p>
  </div>
  <div class="abs page-foot foot-left"><span>www.verdastudio.example</span><span class="page-foot__line"></span><span class="page-foot__num">01</span></div>

  <div class="abs quote-mark quote-open">“</div>
  <p class="abs pull-quote">consectetur<br>adipiscing<br>elit, sed do<br>eiusmod tempor<br>incididunt ut<br>labore et dolore<br>magna aliqua</p>
  <div class="abs quote-mark quote-close">”</div>

  <div class="abs top-rule"></div>
  <h2 class="abs feature-title">LOREM IPSUM<br>DOLOR SIT AMET,<br>CONSECTETUR<br>ADIPISCING ELIT</h2>
  <div class="abs copy feature-copy">
    <p>Lorem ipsum dolor sit amet, consectetur adipiscing elit, sed do eiusmod tempor incididunt ut labore et dolore magna aliqua. Ut enim ad minim veniam, quis nostrud exercitation ullamco laboris nisi ut aliquip ex ea commodo consequat. Duis aute irure dolor in reprehenderit in voluptate velit esse cillum dolore eu fugiat nulla pariatur. Excepteur sint occaecat cupidatat non proident, sunt in culpa qui officia deserunt mollit anim id est laborum.</p>
    <p>Sed ut perspiciatis unde omnis iste natus error sit voluptatem accusantium doloremque laudantium, totam rem aperiam, eaque ipsa quae ab illo inventore veritatis et quasi architecto beatae vitae dicta sunt explicabo. Nemo enim ipsam voluptatem quia voluptas sit aspernatur aut odit aut fugit, sed quia consequuntur magni dolores eos qui ratione voluptatem sequi nesciunt.</p>
  </div>
  <h3 class="abs points-title">Lorem ipsum dolor<br>sit amet, consectetur adipiscing elit</h3>
  <ol class="abs points">
    <li><span class="points__num">1</span><p>sed do eiusmod tempor incididunt ut labore<br>et dolore magna aliqua. Ut enim ad minim<br>veniam, ut aliquip ex ea commodo consequat.</p></li>
    <li><span class="points__num">2</span><p>sed do eiusmod tempor incididunt ut labore<br>et dolore magna aliqua. Ut enim ad minim<br>veniam, ut aliquip ex ea commodo consequat.</p></li>
    <li><span class="points__num">3</span><p>sed do eiusmod tempor incididunt ut labore<br>et dolore magna aliqua. Ut enim ad minim<br>veniam, ut aliquip ex ea commodo consequat.</p></li>
  </ol>
  <div class="abs page-foot foot-right"><span>www.verdastudio.example</span><span class="page-foot__line"></span><span class="page-foot__num">02</span></div>
</section>

</body>
</html>
```